Youth organisation needs design work for awards booklet

We are from The Kestrel Cadet Corps in Singapore, and we need design work for an awards booklet for one of our most prestigious awards, the Lodestar Award. This booklet will comprise of the list of the recipients, congratulatory notes and stories from some of the recipients. This booklet will be printed for each of the recipient to keep as a remembrance. We are looking for dual or tri-colour scheme, with bronze being one of the colours.

Target Market(s)

Recipients of the Award, school Principals and teachers

Requirements
Must have
• We are looking to have around 16 designed pages, including front and back cover. Size of the booklet is:
Closed - W100mm x H210mm; Opened - W200mm x H210mm
Cover page - picture of the Award
Page 2-3 - two congratulatory notes
Page 4-5 - picture of the Award and description of the Award
Page 6-7 - Testimonials
Page 8-14 - List of recipients (to be provided upon confirmation of designer)
Page 15 - blank page or acknowledgments page
Back Cover - KC Logo and contact details
(Refer to previous years' booklets for reference)

Designers can submit just the cover pages as well as 1 sample inner page to get a sense of the overall style of design during the selection round.
Nice to have
• Clean, prestigious/premium look

```html
<!DOCTYPE html>
<html lang="en">
<head>
<meta charset="utf-8">
<title>Lodestar Award Recipients</title>
<link rel="stylesheet" href="https://fonts.googleapis.com/css2?family=Marcellus&family=Archivo:wght@800&family=PT+Sans:wght@700&display=swap">
<style>
  :root {
    --paper-light: #f3e3c2;
    --paper-mid: #e2c793;
    --gold-deep: #b88a2e;
    --gold-mid: #e0b84a;
    --gold-bright: #fbe58a;
    --bronze-dark: #221a13;
    --bronze: #6e4c37;
    --ink: #111111;
    --divider: #9a6a3a;
  }
  * { margin: 0; padding: 0; box-sizing: border-box; }
  html, body { width: 1143px; height: 1200px; overflow: hidden; }
  body {
    position: relative;
    background:
      radial-gradient(ellipse 500px 400px at 85% 90%, rgba(255,245,210,0.9), transparent 70%),
      radial-gradient(ellipse 600px 500px at 50% 40%, var(--paper-light), transparent 80%),
      linear-gradient(160deg, var(--paper-mid), var(--paper-light) 45%, #d9b874 100%);
    font-family: "PT Sans", sans-serif;
    font-weight: 700;
    color: var(--ink);
  }
  .spread-divider {
    position: absolute; left: 571px; top: 0; width: 1px; height: 1200px;
    background: var(--divider);
  }
  .panel {
    position: absolute;
    background:
      radial-gradient(ellipse 60% 30% at 50% 20%, rgba(255,246,170,0.8), transparent 70%),
      radial-gradient(ellipse 60% 30% at 50% 60%, rgba(255,240,150,0.7), transparent 70%),
      linear-gradient(90deg, var(--gold-deep), var(--gold-mid) 20%, var(--gold-bright) 50%, var(--gold-mid) 80%, var(--gold-deep));
    box-shadow: 0 6px 14px rgba(80,50,20,0.35);
  }
  .panel--left { left: 32px; top: 30px; width: 504px; height: 1142px; }
  .panel--right { left: 615px; top: 30px; width: 503px; height: 871px; }

  .masthead {
    position: absolute; left: 0; top: 0; width: 100%; height: 134px;
    background:
      radial-gradient(ellipse 160px 70px at 62% 0%, rgba(255,190,60,0.85), transparent 80%),
      linear-gradient(90deg, var(--bronze-dark) 8%, #3a2c20 30%, var(--bronze) 100%);
    text-align: center;
  }
  .masthead__title {
    font-family: "Marcellus", serif;
    font-weight: 400;
    color: #fbf3df;
    text-shadow: 0 2px 4px rgba(0,0,0,0.6);
    padding-top: 14px;
    padding-left: 10px;
  }
  .masthead__title .line-1 { display: block; font-size: 70px; line-height: 64px; letter-spacing: 5px; }
  .masthead__title .line-2 { display: block; font-size: 37px; line-height: 40px; letter-spacing: 3px; }
  .intro {
    position: absolute; left: 0; top: 134px; width: 100%;
    text-align: center; font-size: 19px; line-height: 27px;
  }

  .company { position: absolute; width: 100%; }
  .company__bar {
    position: absolute; left: 33px; top: 0; width: 420px; height: 52px;
    background:
      radial-gradient(ellipse 140px 30px at 55% 0%, rgba(255,200,80,0.7), transparent 80%),
      linear-gradient(90deg, var(--bronze-dark), #3b2d21 40%, var(--bronze));
    font-family: "Archivo", sans-serif; font-weight: 800;
    font-size: 28px; line-height: 52px; letter-spacing: -1.2px;
    padding-left: 17px; white-space: nowrap;
  }
  .panel--right .company__bar { left: 29px; padding-left: 30px; }
  .company__name {
    background: linear-gradient(180deg, #fff8e0 0%, #e9d6a8 55%, #b79a62 100%);
    -webkit-background-clip: text; background-clip: text; color: transparent;
    filter: drop-shadow(0 2px 2px rgba(0,0,0,0.7));
  }
  .company__name sup { font-size: 15px; vertical-align: 11px; letter-spacing: 0; }
  .company__unit {
    position: absolute; left: 0; top: 57px; width: 100%;
    text-align: center; font-size: 19.5px; line-height: 20px;
  }
  .company__unit .school { display: block; padding-right: 54px; }
  .company__unit .church { display: block; }
  .recipients { position: absolute; left: 12px; top: 116px; width: 480px; font-size: 19.5px; line-height: 21px; white-space: nowrap; }
  .recipients__col { position: absolute; top: 0; }
  .recipients__col--main { left: 0; }
  .recipients__col--side { left: 265px; padding-left: 12px; border-left: 2px solid var(--ink); height: 56px; }
  .panel--right .recipients { left: 21px; top: 122px; line-height: 27px; }
  .panel--right .recipients__col--side { left: 240px; padding-left: 18px; height: 58px; line-height: 23px; }
  .panel--right .company__unit { top: 58px; line-height: 23px; }
  .panel--right .recipients--compact, .panel--right .recipients--compact .recipients__col--side { line-height: 21px; }
</style>
</head>
<body>
  <div class="spread-divider"></div>

  <section class="panel panel--left">
    <header class="masthead">
      <h1 class="masthead__title"><span class="line-1">LODESTAR</span><span class="line-2">AWARD RECIPIENTS</span></h1>
    </header>
    <p class="intro">This year we are proud to present the<br>THE LODESTAR AWARD to the following recipients</p>

    <div class="company" style="top:209px">
      <div class="company__bar"><span class="company__name">2<sup>nd</sup> NORTHPORT COMPANY</span></div>
      <p class="company__unit"><span class="school">HARBOURVIEW SCHOOL</span><span class="church">TELOK AYER GRACE CHURCH</span></p>
      <div class="recipients">
        <div class="recipients__col recipients__col--main">SSG DARREN LOW<br>SSG TAN WEI JIE<br>SSG MARCUS LIM JUN HAO</div>
        <div class="recipients__col recipients__col--side">SSG DARREN LOW<br>SSG DARREN LOW</div>
      </div>
    </div>

    <div class="company" style="top:457px">
      <div class="company__bar"><span class="company__name">3<sup>rd</sup> NORTHPORT COMPANY</span></div>
      <p class="company__unit"><span class="school">HARBOURVIEW SCHOOL</span><span class="church">TELOK AYER GRACE CHURCH</span></p>
      <div class="recipients">
        <div class="recipients__col recipients__col--main">SSG DARREN LOW<br>SSG TAN WEI JIE<br>SSG MARCUS LIM JUN HAO</div>
        <div class="recipients__col recipients__col--side">SSG DARREN LOW<br>SSG DARREN LOW</div>
      </div>
    </div>

    <div class="company" style="top:693px">
      <div class="company__bar"><span class="company__name">4<sup>th</sup> NORTHPORT COMPANY</span></div>
      <p class="company__unit"><span class="school">HARBOURVIEW SCHOOL</span><span class="church">TELOK AYER GRACE CHURCH</span></p>
      <div class="recipients">
        <div class="recipients__col recipients__col--main">SSG DARREN LOW<br>SSG TAN WEI JIE<br>SSG MARCUS LIM JUN HAO</div>
        <div class="recipients__col recipients__col--side">SSG DARREN LOW<br>SSG DARREN LOW</div>
      </div>
    </div>

    <div class="company" style="top:931px">
      <div class="company__bar"><span class="company__name">5<sup>th</sup> NORTHPORT COMPANY</span></div>
      <p class="company__unit"><span class="school">HARBOURVIEW SCHOOL</span><span class="church">TELOK AYER GRACE CHURCH</span></p>
      <div class="recipients">
        <div class="recipients__col recipients__col--main">SSG DARREN LOW<br>SSG TAN WEI JIE<br>SSG MARCUS LIM JUN HAO</div>
        <div class="recipients__col recipients__col--side">SSG DARREN LOW<br>SSG DARREN LOW</div>
      </div>
    </div>
  </section>

  <section class="panel panel--right">
    <div class="company" style="top:66px">
      <div class="company__bar"><span class="company__name">6<sup>th</sup> NORTHPORT COMPANY</span></div>
      <p class="company__unit"><span class="school">HARBOURVIEW SCHOOL</span><span class="church">TELOK AYER GRACE CHURCH</span></p>
      <div class="recipients">
        <div class="recipients__col recipients__col--main">SSG DARREN LOW<br>SSG TAN WEI JIE<br>SSG MARCUS LIM JUN HAO</div>
        <div class="recipients__col recipients__col--side">SSG DARREN LOW<br>SSG DARREN LOW</div>
      </div>
    </div>

    <div class="company" style="top:317px">
      <div class="company__bar"><span class="company__name">7<sup>th</sup> NORTHPORT COMPANY</span></div>
      <p class="company__unit"><span class="school">HARBOURVIEW SCHOOL</span><span class="church">TELOK AYER GRACE CHURCH</span></p>
      <div class="recipients">
        <div class="recipients__col recipients__col--main">SSG DARREN LOW<br>SSG TAN WEI JIE<br>SSG MARCUS LIM JUN HAO</div>
        <div class="recipients__col recipients__col--side">SSG DARREN LOW<br>SSG DARREN LOW</div>
      </div>
    </div>

    <div class="company" style="top:594px">
      <div class="company__bar"><span class="company__name">8<sup>th</sup> NORTHPORT COMPANY</span></div>
      <p class="company__unit"><span class="school">HARBOURVIEW SCHOOL</span><span class="church">TELOK AYER GRACE CHURCH</span></p>
      <div class="recipients recipients--compact">
        <div class="recipients__col recipients__col--main">SSG DARREN LOW<br>SSG TAN WEI JIE<br>SSG MARCUS LIM JUN HAO</div>
        <div class="recipients__col recipients__col--side">SSG DARREN LOW<br>SSG DARREN LOW</div>
      </div>
    </div>
  </section>
</body>
</html>
```